Non-profit organization requires InDesign based template for a educational booklet

***Overview***
Our business "The Southern Meridian Collective for Skills and Growth" is a not for profit organisation working in vocational education both in the Australian and international markets. While we work within many professional contexts, we also work with projects in developing countries assisting to build institutional capacity in the education industry, upskilling in disadvantaged communities to ultimately facilitate positive development outcomes.

Our project is looking to deliver agricultural-based education units that will be delivered in booklet form. Vocational students will use these unit booklets for self-paced or classroom group study. The front of each unit will have a nice graphical cover page, contents and details about learning in the unit. This will be followed by about 15 pages of educational content with plenty of pictures and other material such as tables and graphs to illustrate learning points. This will then be followed by a short question sheet with space for students to write answers, followed by Activity sheets where students put into practice skills from the unit.

***The designed template should have***
* Cover page;
* Content page;
* Two (2) different introduction pages (two for variation);
* Three (3) different pages for lesson text – these pages will be the main study pages for the students, 3 for variation;
* Activity page - like an activity worksheet;
* Question page - page with questions or reflections that the students need to answer - a space under each question for students to write;

***Design preferences***

*Font – an inDesign default font please like Calibri – text built on a base Normal font 11pt, then headings H1, H2 etc... from that basis e.g. 24pt for H1 etc... the size up to the designer.

Happy to see creativity of graphic artists with the above themes.

Target Market(s)

In the requested project, I require an Adobe InDesign template (file in .indd) to be designed that will have particular characteristics suited to students who are:

* Age 15-17;
* Have the educational equivalent to Australian and US education standard of Yr 8;
* Attending vocational school - vocational schools are between secondary high school and University and are usually used to produce graduates within the skill trade area;
* Agricultural theme in the template;
* Sustainability theme (agricultural sustainability) as well;

Students are from very poor rural farming families in growing rice, coconut, rambutan, mangoes, cocoa, palm oil... - very SE Asian agricultural landscape.

Students are used to black and white government textbooks which are very dry, largely dull in design and colour – we do not want this!

Industry/Entity Type

Agriculture

Font styles to use
Sans Serif

Colors

Designer to choose colors to be used in the design.

Requirements
Must have
• * Final file must be in an editable Adobe Indesign file (.indd), with editable layers;
• * SE Asian agricultural theme in the template;
• * design must not look like dull and boring textbooks or corporate training booklets; * design should be vibrant and interesting but also not distracting from the lesson (i.e. it is not too garish);
• * suitable colours (it will be printed full colour) easy on the eye for students of the age group - colours related to agriculture;
• *Modern look and feel;
Should not have
• * design must not look like dull and boring textbooks or corporate training booklets;

```html
<!DOCTYPE html>
<html lang="en">
<head>
<meta charset="utf-8">
<title>Agricultural Education Booklet Template</title>
<link href="https://fonts.googleapis.com/css2?family=Open+Sans:ital,wght@0,300;0,400;0,600;0,700;1,300;1,400;1,600;1,700&display=swap" rel="stylesheet">
<style>
:root{
  --backdrop:#c9c9c9;
  --paper:#ffffff;
  --leaf:#7aa83f;
  --sky:#1f6fb2;
  --sky-pale:#dde6f1;
  --slate:#6d6e71;
  --ink:#231f20;
  --ink-soft:#555;
}
*{box-sizing:border-box;margin:0;padding:0}
html,body{width:1200px;height:1200px;overflow:hidden;background:var(--backdrop)}
body{font-family:"Open Sans",Arial,sans-serif;color:var(--ink)}
.canvas{position:relative;width:1200px;height:1200px;overflow:hidden;background:var(--backdrop)}
.abs{position:absolute}
.page{position:absolute;background:var(--paper);overflow:hidden}
.photo{position:absolute}
.micro{position:absolute;font-size:4.2px;line-height:5.5px;color:var(--ink);overflow:hidden;text-align:left}
.micro h4{font-size:4.6px;line-height:5.6px;color:var(--sky);font-weight:700;margin:3px 0 1px;text-transform:uppercase}
.micro h5{font-size:4.6px;line-height:5.6px;color:var(--ink-soft);font-weight:400;margin:3px 0 1px;text-transform:uppercase}
.micro p{margin-bottom:3px}
.micro-cap{position:absolute;font-size:3.8px;line-height:4.6px;font-style:italic;font-weight:700;color:var(--ink)}
.mini-title{position:absolute;font-weight:300;color:var(--ink);font-size:11.5px;line-height:14px;letter-spacing:.2px}
.mini-tag{position:absolute;font-size:5px;font-weight:700;color:var(--leaf);letter-spacing:.3px}
.mini-rule{position:absolute;height:1.5px;background:var(--leaf)}
.mini-foot{position:absolute;font-size:4px;font-style:italic;color:var(--ink-soft);letter-spacing:.2px}
.folio{position:absolute;border-radius:50%;background:var(--slate);color:#fff;text-align:center;font-weight:300}
.folio-sm{width:16px;height:16px;font-size:6.5px;line-height:16px}
.brand-sq{position:absolute;width:9px;height:9px}
.brand-name{position:absolute;font-size:3.8px;line-height:4.4px;font-weight:600}
.mini-table{position:absolute;border-collapse:collapse;font-size:3.5px;line-height:4.4px}
.mini-table th{background:var(--sky);color:#fff;font-weight:700;text-align:left;padding:0 2px}
.mini-table td{padding:0 2px;border-bottom:.4px solid #bbb}
.mini-table tr:nth-child(odd) td{background:var(--sky-pale)}
.mini-table-cap{position:absolute;font-size:4px;font-weight:700}
.mini-side-item{position:absolute;font-size:4px;line-height:5.2px;color:#fff}
.mini-side-item b{position:absolute;left:-9px;top:0;width:7px;height:7px;border-radius:50%;background:#fff;font-size:4px;line-height:7px;text-align:center}
.mini-quote{position:absolute;border-radius:50%;background:#fff;text-align:center;font-style:italic;font-weight:300;font-size:5px;line-height:7px;display:flex;align-items:center;justify-content:center}
.chart-box{position:absolute;background:#fff;border:1px solid #d8d8d8}
.chart-box svg{position:absolute;inset:4px}

/* cover */
.cover{position:absolute;left:42px;top:80px;width:164px;height:231px;background:var(--sky);overflow:hidden}
.cover-field{left:0;top:0;width:96px;height:231px;background:linear-gradient(180deg,#6b7f3a 0%,#9aa55a 40%,#b08a5c 60%,#6e4f33 100%)}
.cover-band{left:0;top:150px;width:164px;height:81px;background:linear-gradient(180deg,#b9945f,#7a5a3a)}
.cover-panel{left:96px;top:0;width:68px;height:150px;background:var(--sky)}
.cover-dot{left:134px;top:14px;width:12px;height:12px;border-radius:50%;background:#fff}
.cover-name{left:106px;top:30px;width:54px;font-size:3.6px;line-height:4.3px;color:#fff;font-weight:600;text-align:center}
.cover-edu{left:26px;top:140px;font-size:9px;font-style:italic;color:#222;font-weight:400;background:rgba(255,255,255,.85);padding:0 3px}
.cover-agri{left:76px;top:209px;font-size:10.5px;font-style:italic;font-weight:700;color:#fff;letter-spacing:.3px}

/* main spread */
.spread-main{left:46px;top:376px;width:1118px;height:807px;background:var(--paper);overflow:hidden}
.hdr-band{left:34px;top:0;width:492px;height:96px;background:var(--leaf)}
.hdr-brand{left:0;top:0;width:90px;height:108px;background:var(--sky)}
.hdr-brand-name{left:8px;top:38px;width:76px;color:#fff;font-size:8px;line-height:10px;font-weight:600}
.hdr-rule{left:0;top:102px;width:570px;height:7px;background:var(--sky)}
.hdr-tag{left:93px;top:31px;color:#fff;font-weight:700;font-size:14px;letter-spacing:.8px}
.hdr-title{left:108px;top:52px;color:#fff;font-weight:300;font-size:31px;line-height:36px;letter-spacing:.6px}

.side-panel{left:30px;top:148px;width:164px;height:610px;background:var(--sky)}
.side-item{position:absolute;left:30px;width:130px;color:#fff;font-size:9.4px;line-height:14.2px}
.side-num{position:absolute;left:-20px;top:0;width:15px;height:15px;border-radius:50%;background:#fff;color:var(--sky);font-weight:700;font-size:9px;line-height:15px;text-align:center}
.side-quote{position:absolute;width:136px;height:136px;border-radius:50%;background:#fff;color:var(--ink-soft);font-style:italic;font-weight:300;font-size:13.5px;line-height:24px;text-align:center;display:flex;align-items:center;justify-content:center}

.hero-photo{left:194px;top:148px;width:332px;height:248px;background:linear-gradient(180deg,#8fb3d6 0%,#b9cfe0 18%,#6f7d58 28%,#9b8a6a 45%,#b39470 70%,#8e7253 100%)}
.hero-cap{left:330px;top:158px;width:190px;text-align:right;color:#fff;font-style:italic;font-weight:700;font-size:10.5px;line-height:14px}

.body-col{position:absolute;font-size:9.4px;line-height:12.8px;color:var(--ink);overflow:hidden}
.body-col p{margin-bottom:12.8px}
.dropcap{float:left;font-size:36px;line-height:30px;font-weight:300;font-style:italic;color:var(--ink);margin:2px 6px 0 0}
.h2-blue{color:var(--sky);font-weight:600;font-size:11.5px;line-height:15px;text-transform:uppercase;margin:0 0 1px}
.h3-grey{color:var(--ink-soft);font-weight:400;font-size:10.5px;line-height:14px;text-transform:uppercase;margin:0 0 1px}

.tbl-cap{left:613px;top:46px;font-weight:700;font-size:11px;letter-spacing:.1px}
.data-table{position:absolute;left:613px;top:60px;width:483px;border-collapse:collapse;font-size:10px}
.data-table th{background:var(--sky);color:#fff;font-weight:700;height:15px;padding:0 8px;text-align:left;font-size:9.5px}
.data-table td{height:15.6px;padding:0 8px;border-bottom:1px solid #b9c4d2}
.data-table tr:nth-child(even) td{background:var(--sky-pale)}
.data-table .c-h{width:85px;text-align:center}
.data-table .c-t{width:100px;text-align:right;padding-right:12px}

.chart-cap{position:absolute;font-size:9.5px;line-height:12.8px;font-style:italic;font-weight:700}
.main-foot{position:absolute;top:780px;font-size:11px;font-style:italic;color:var(--ink-soft);letter-spacing:.4px}
.folio-lg{width:40px;height:40px;font-size:16px;line-height:40px}
</style>
</head>
<body>
<div class="canvas">

<svg width="0" height="0" style="position:absolute" aria-hidden="true">
  <defs>
    <symbol id="pie" viewBox="0 0 100 100">
      <path d="M50 50L50 0A50 50 0 0 1 58.7 0.8Z" fill="#4472c4"/>
      <path d="M50 50L58.7 0.8A50 50 0 0 1 65.5 2.4Z" fill="#ed7d31"/>
      <path d="M50 50L65.5 2.4A50 50 0 0 1 70.3 4.3Z" fill="#a5a5a5"/>
      <path d="M50 50L70.3 4.3A50 50 0 0 1 76.5 7.6Z" fill="#ffc000"/>
      <path d="M50 50L76.5 7.6A50 50 0 0 1 83.5 12.8Z" fill="#5b9bd5"/>
      <path d="M50 50L83.5 12.8A50 50 0 0 1 90.5 20.6Z" fill="#70ad47"/>
      <path d="M50 50L90.5 20.6A50 50 0 0 1 98.1 36.2Z" fill="#264478"/>
      <path d="M50 50L98.1 36.2A50 50 0 0 1 99.9 53.5Z" fill="#9e480e"/>
      <path d="M50 50L99.9 53.5A50 50 0 0 1 97.3 66.3Z" fill="#636363"/>
      <path d="M50 50L97.3 66.3A50 50 0 0 1 88.9 81.5Z" fill="#997300"/>
      <path d="M50 50L88.9 81.5A50 50 0 0 1 75.8 92.9Z" fill="#255e91"/>
      <path d="M50 50L75.8 92.9A50 50 0 0 1 63.8 98.1Z" fill="#43682b"/>
      <path d="M50 50L63.8 98.1A50 50 0 0 1 9.5 79.4Z" fill="#d0605a"/>
      <path d="M50 50L9.5 79.4A50 50 0 0 1 50 0Z" fill="#9bbb59"/>
    </symbol>
    <symbol id="bars" viewBox="0 0 300 190">
      <g stroke="#e2e2e2" stroke-width="1">
        <line x1="20" y1="10" x2="270" y2="10"/><line x1="20" y1="40" x2="270" y2="40"/>
        <line x1="20" y1="70" x2="270" y2="70"/><line x1="20" y1="100" x2="270" y2="100"/>
        <line x1="20" y1="130" x2="270" y2="130"/><line x1="20" y1="160" x2="270" y2="160"/>
      </g>
      <rect x="24" y="22" width="82" height="160" fill="#4472c4"/>
      <rect x="108" y="164" width="160" height="18" fill="#4472c4"/>
      <polyline points="30,36 110,20 190,12 266,8" fill="none" stroke="#d04a3a" stroke-width="1.6"/>
      <line x1="20" y1="182" x2="270" y2="182" stroke="#999" stroke-width="1"/>
      <g font-size="8" fill="#777" font-family="Open Sans, sans-serif">
        <text x="4" y="14">12</text><text x="4" y="74">8</text><text x="4" y="134">4</text><text x="4" y="184">0</text>
        <text x="274" y="14">100%</text><text x="274" y="74">60%</text><text x="274" y="134">20%</text><text x="274" y="184">0%</text>
      </g>
    </symbol>
  </defs>
</svg>

<!-- COVER -->
<section class="cover" aria-label="Cover page">
  <div class="photo abs cover-field" role="img" aria-label="Young green crop leaves and a grazing cow on farmland"></div>
  <div class="photo abs cover-band" role="img" aria-label="Ploughed field soil"></div>
  <div class="abs cover-panel"></div>
  <div class="abs cover-dot"></div>
  <div class="abs cover-name">The Southern Meridian Collective for Skills and Growth</div>
  <div class="abs cover-edu">EDUCATION</div>
  <div class="abs cover-agri">AGRICULTURAL</div>
</section>

<!-- SPREAD PAGES 8–9 -->
<section class="page" style="left:218px;top:19px;width:236px;height:340px" aria-label="Lesson page 8">
  <div class="brand-sq" style="left:4px;top:8px;background:var(--leaf)"></div>
  <div class="brand-name" style="left:4px;top:19px;width:42px;color:var(--leaf)">The Southern Meridian Collective for Skills and Growth</div>
  <div class="mini-title" style="left:48px;top:14px">2.1 DECTUS PES IA CONSUL</div>
  <div class="mini-rule" style="left:46px;top:40px;width:190px"></div>
  <div class="mini-tag" style="left:48px;top:42px">TRAINING</div>
  <div class="micro" style="left:20px;top:58px;width:62px;height:176px">
    <p>Losta, perarebute es audees ego con habultum dem mo ex sulica; etrestr obuncles, veremqui con sentem praccie nteatum silictur. At inatamp liusque tastrem catil tam intim pat in nonscerei publicit iam pere nonsum iuris.</p>
    <h4>Escis omne nonequam in vatquam sidions con etra? Que init.</h4>
    <p>Utem ocrit? Tum diis. Riaelin gultus ilicuppl. Pimmort eriusquos me prae tum clem porumena, prit aperestis essa es me nonsultorum. Rommo potiferet? Oc rem in si egitisse artum fac rest ponenatus patquame descest ionclab erfercem nit videfac erferidicae videorbitu esciti sen aucons es! Supicatina, consuli cieniur aric remquas traessil clabus rebusquos de adet atiaed mordius mae terit.</p>
  </div>
  <div class="micro" style="left:88px;top:58px;width:68px;height:176px">
    <p>Nam rei peremrpor iam vivereb usatuidit, quost vid sus ne no.</p>
    <p>Gra, orum qui publiceritis vium acte nonsit vid constata restam inius culturatus. Ont ata pati, pata ductario, concerris ventrideo et etiamperdius iamquem potiurox ne nisse, quius rei faccibu squius, ductabi stemus, que contri, nonfeconeque acte es rei tessidiendum diurnih ilicavolus.</p>
    <h5>Opioc, condi poeruntudam host L.</h5>
    <p>Bem sa num imum sus ad inte conerfesil veroximaxime cre, cesseni munterebent? Ad inati, patientem noniae porum, unte egit; et iam alis, adem duconsc epopublii temeniusat estem is horuntes et addum tatum fat, nerehenat L. Nihi, caut duci in diensil.</p>
  </div>
  <div class="abs" style="left:163px;top:45px;width:73px;height:200px;background:var(--leaf)"></div>
  <div class="mini-side-item" style="left:178px;top:50px;width:54px"><b style="color:var(--leaf)">1</b>Losta, perarebute es audees ego con habultum dem mo ex sulica; etrestr obuncles.</div>
  <div class="mini-side-item" style="left:178px;top:90px;width:54px"><b style="color:var(--leaf)">2</b>Dectus pes ia consul vil condiem perfeces sena, nius faudam nonsula bernit.</div>
  <div class="mini-side-item" style="left:178px;top:130px;width:54px"><b style="color:var(--leaf)">3</b>Losta, perarebute es audees ego con habultum dem mo ex sulica; etrestr obuncles.</div>
  <div class="mini-side-item" style="left:178px;top:170px;width:54px"><b style="color:var(--leaf)">4</b>Dectus pes ia consul vil condiem perfeces sena, nius faudam nonsula bernit.</div>
  <div class="mini-quote" style="left:170px;top:246px;width:56px;height:56px;color:var(--ink-soft);border:1px solid #e4e4e4">Escis omne<br>nonequam in<br>vatquam sidions<br>con Etra?</div>
  <div class="mini-table-cap" style="left:20px;top:238px">ESCIS OMNE NONEQUAM IN VATQUAM SIDIONS CON ETRA?</div>
  <table class="mini-table" style="left:20px;top:245px;width:130px">
    <tr><th>HOURS</th><th>DESCRIPTION</th><th>TOTAL</th></tr>
    <tr><td>1,25</td><td>Butelis ficuppl inprore atiam</td><td>562,50</td></tr>
    <tr><td>0,50</td><td>Inum terum patus dumus?</td><td>225,00</td></tr>
    <tr><td>0,50</td><td>Fir ad inatus facerid mentiam</td><td>225,00</td></tr>
    <tr><td>0,50</td><td>Butelis ficuppl inprore atiam</td><td>225,00</td></tr>
    <tr><td>3,00</td><td>Butelis ficuppl inprore atiam</td><td>1 350,00</td></tr>
    <tr><td>3,00</td><td>Inum terum patus dumus?</td><td>1 350,00</td></tr>
    <tr><td>0,50</td><td>Fir ad inatus facerid mentiam</td><td>225,00</td></tr>
    <tr><td>0,50</td><td>Butelis ficuppl inprore atiam</td><td>225,00</td></tr>
  </table>
  <div class="folio folio-sm" style="left:4px;top:322px">8</div>
  <div class="mini-foot" style="left:24px;top:328px">TRAINING AND DEVELOPMENT</div>
</section>

<section class="page" style="left:454px;top:19px;width:236px;height:340px" aria-label="Lesson page 9">
  <div class="chart-box" style="left:22px;top:14px;width:132px;height:84px;border:none">
    <svg width="124" height="76" aria-hidden="true"><use href="#bars"/></svg>
  </div>
  <div class="micro-cap" style="left:22px;top:100px;width:134px">Ehenis ma quis et voluptas et lit quibus et eum inctat. Genet pelest abo. Loratusdant, temqui blaborert</div>
  <div class="chart-box" style="left:22px;top:112px;width:132px;height:116px">
    <svg width="124" height="108" aria-hidden="true"><use href="#pie"/></svg>
  </div>
  <div class="micro-cap" style="left:22px;top:230px;width:134px">Ehenis ma quis et voluptas et lit quibus et eum inctat. Genet pelest abo. Loratusdant, temqui blaborert</div>
  <div class="photo" style="left:22px;top:242px;width:132px;height:78px;background:linear-gradient(180deg,#9bb7d2 0%,#7d8a5e 30%,#a98b66 60%,#87694a 100%)" role="img" aria-label="Farmer inspecting soil in a dry field"></div>
  <svg class="abs" style="left:22px;top:242px" width="132" height="40" aria-hidden="true"><polygon points="0,0 80,0 0,34" fill="#7aa83f"/></svg>
  <div class="micro-cap" style="left:25px;top:245px;width:50px;color:#fff">Ehenis ma quis et voluptas et lit quibus et eum inctat.</div>
  <div class="micro" style="left:162px;top:14px;width:68px;height:300px">
    <h4 style="margin-top:0">Escis omne nonequam in vatquam sidions con etra? Que init.</h4>
    <p>Utem ocrit? Tum diis. Riaelin gultus ilicuppl. Pimmort eriusquos me prae tum clem porumena, prit aperestis essa es me nonsultorum. Rommo potiferet? Oc rem in si egitisse artum fac rest ponenatus patquame descest ionclab erfercem nit videfac erferidicae videorbitu esciti sen aucons es! Supicatina, consuli cieniur aric remquas traessil clabus rebusquos de adet atiaed mordius.</p>
    <p>Vales! Quam vit deatum cae propul hum tam it. Inum terum patus dumus? Pati se publiis. Vivit que tantiu sentissi pulibunces ahala pultus iam effre patorte riorit.</p>
    <p>Gra, orum qui publiceritis vium acte nonsit vid constata restam inius culturatus. Ont ata pati, pata ductario, concerris ventrideo et etiamperdius iamquem potiurox ne nisse, quius rei faccibu squius.</p>
    <h5>Opioc, condi poeruntudam host L.</h5>
    <p>Bem sa num imum sus ad inte conerfesil veroximaxime cre, cesseni munterebent? Ad inati, patientem noniae porum, unte egit; et iam alis, adem duconsc epopublii temeniusat estem is horuntes et addum tatum fat, nerehenat L. Nihi, caut L. Bonsultodi, nesserid ia et? Natia duci in diensil uterfic avoccibust?</p>
  </div>
  <div class="mini-foot" style="left:148px;top:328px">TRAINING AND DEVELOPMENT</div>
  <div class="folio folio-sm" style="left:214px;top:322px">9</div>
</section>

<!-- SPREAD PAGES 10–11 -->
<section class="page" style="left:702px;top:19px;width:230px;height:340px" aria-label="Lesson page 10">
  <div class="abs" style="left:0;top:0;width:78px;height:340px;background:var(--slate)"></div>
  <div class="brand-sq" style="left:6px;top:8px;background:#fff"></div>
  <div class="brand-name" style="left:6px;top:19px;width:60px;color:#fff">The Southern Meridian Collective for Skills and Growth</div>
  <div class="mini-title" style="left:79px;top:10px">3.1 DECTUS PES SAD<br>&nbsp;&nbsp;&nbsp;&nbsp;IA CONSUL AS?</div>
  <div class="mini-rule" style="left:78px;top:46px;width:152px"></div>
  <div class="mini-tag" style="left:120px;top:38px">TRAINING</div>
  <div class="mini-side-item" style="left:20px;top:84px;width:54px"><b style="color:var(--slate)">1</b>Losta, perarebute es audees ego con habultum dem mo ex sulica; etrestr obuncles.</div>
  <div class="mini-side-item" style="left:20px;top:124px;width:54px"><b style="color:var(--slate)">2</b>Dectus pes ia consul vil condiem perfeces sena, nius faudam nonsula bernit.</div>
  <div class="mini-side-item" style="left:20px;top:164px;width:54px"><b style="color:var(--slate)">3</b>Losta, perarebute es audees ego con habultum dem mo ex sulica; etrestr obuncles.</div>
  <div class="mini-side-item" style="left:20px;top:204px;width:54px"><b style="color:var(--slate)">4</b>Dectus pes ia consul vil condiem perfeces sena, nius faudam nonsula bernit.</div>
  <div class="mini-quote" style="left:10px;top:264px;width:56px;height:56px;color:var(--leaf)">Escis omne<br>nonequam in<br>vatquam sidions<br>con Etra?</div>
  <div class="micro" style="left:82px;top:56px;width:68px;height:180px">
    <p>Losta, perarebute es audees ego con habultum dem mo ex sulica; etrestr obuncles, veremqui con sentem praccie nteatum silictur. At inatamp liusque tastrem catil tam intim pat in nonscerei publicit iam pere nonsum iuris.</p>
    <h4>Escis omne nonequam in vatquam sidions con etra? Que init.</h4>
    <p>Utem ocrit? Tum diis. Riaelin gultus ilicuppl. Pimmort eriusquos me prae tum clem porumena, prit aperestis essa es me nonsultorum. Rommo potiferet? Oc rem in si egitisse artum fac rest ponenatus patquame descest ionclab erfercem nit videfac erferidicae videorbitu esciti sen aucons es! Supicatina, consuli cieniur aric remquas traessil clabus rebusquos de adet.</p>
  </div>
  <div class="micro" style="left:156px;top:56px;width:70px;height:180px">
    <p>Nam rei peremrpor iam vivereb usatuidit, quost vid sus ne no.</p>
    <p>Gra, orum qui publiceritis vium acte nonsit vid constata restam inius culturatus. Ont ata pati, pata ductario, concerris ventrideo et etiamperdius iamquem potiurox ne nisse, quius rei faccibu squius, ductabi stemus, que contri.</p>
    <h5>Opioc, condi poeruntudam host L.</h5>
    <p>Bem sa num imum sus ad inte conerfesil veroximaxime cre, cesseni munterebent? Ad inati, patientem noniae porum, unte egit; et iam alis, adem duconsc epopublii temeniusat estem is horuntes et addum.</p>
    <p>Gra, orum qui publiceritis vium acte nonsit vid constata restam inius culturatus.</p>
  </div>
  <div class="mini-table-cap" style="left:80px;top:238px">ESCIS OMNE NONEQUAM IN VATQUAM SIDIONS CON ETRA?</div>
  <table class="mini-table" style="left:80px;top:245px;width:146px">
    <tr><th>HOURS</th><th>DESCRIPTION</th><th>TOTAL</th></tr>
    <tr><td>1,25</td><td>Butelis ficuppl inprore atiam</td><td>562,50</td></tr>
    <tr><td>0,50</td><td>Inum terum patus dumus?</td><td>225,00</td></tr>
    <tr><td>0,50</td><td>Fir ad inatus facerid mentiam</td><td>225,00</td></tr>
    <tr><td>0,50</td><td>Butelis ficuppl inprore atiam</td><td>225,00</td></tr>
    <tr><td>3,00</td><td>Butelis ficuppl inprore atiam</td><td>1 350,00</td></tr>
    <tr><td>3,00</td><td>Inum terum patus dumus?</td><td>1 350,00</td></tr>
    <tr><td>0,50</td><td>Fir ad inatus facerid mentiam</td><td>225,00</td></tr>
    <tr><td>0,50</td><td>Butelis ficuppl inprore atiam</td><td>225,00</td></tr>
  </table>
  <div class="folio folio-sm" style="left:2px;top:322px">10</div>
  <div class="mini-foot" style="left:84px;top:328px">TRAINING AND DEVELOPMENT</div>
</section>

<section class="page" style="left:932px;top:19px;width:230px;height:340px" aria-label="Lesson page 11">
  <div class="micro" style="left:16px;top:6px;width:66px;height:50px">
    <p>tatum fat, nerehenat L. Nihi, caut L. Bonsultodi, nesserid ia et? Natia duci in diensil uterfic avoccibust? Fir ad inatus facerid mentiam dientia nonsign artius omne achilic muri.</p>
  </div>
  <div class="micro" style="left:88px;top:6px;width:66px;height:50px">
    <p>aperestis essa es me nonsultorum Rommo potiferet? Oc rem in si egitisse artum fac rest ponenatus patquame descest ionclab erfercem nit videfac erferidicae vide.</p>
  </div>
  <div class="chart-box" style="left:16px;top:58px;width:138px;height:92px;border:none">
    <svg width="130" height="84" aria-hidden="true"><use href="#pie"/></svg>
  </div>
  <div class="micro-cap" style="left:16px;top:152px;width:138px">Ehenis ma quis et voluptas et lit quibus et eum inctat. Genet pelest abo. Loratusdant, temqui blaborert</div>
  <div class="micro" style="left:16px;top:168px;width:66px;height:68px">
    <p>parei pro, nem acericiam urbit, morur hil sedius coniquam mentios considerfec movivirtesum tuit, es molum perei simur. Verudem</p>
    <h4>Escis omne nonequam in vatquam sidions con etra? Que init.</h4>
    <p>Utem ocrit? Tum diis. Riaelin gultus ilicuppl. Pimmort eriusquos me prae tum clem porumena.</p>
  </div>
  <div class="micro" style="left:88px;top:168px;width:66px;height:68px">
    <p>orbitu esciti sen aucons es! Supicatina, consuli cieniur aric remquas traessil clabus rebusquos de adet atiaed mordius mae terit, quem st iu it, confirmis, vives! Ifecon dissens consus et viderium queris. Butelis ficuppl inprore comnicaude atiam nintimus iam coere ingulto utus, Ti.</p>
    <p>Vales! Quam vit deatum cae propul hum tam it.</p>
  </div>
  <div class="photo" style="left:0;top:239px;width:118px;height:78px;background:linear-gradient(180deg,#a9c2d8 0%,#7f8c60 30%,#a88a66 60%,#86684a 100%)" role="img" aria-label="Farmer inspecting soil in a dry field"></div>
  <svg class="abs" style="left:0;top:239px" width="118" height="40" aria-hidden="true"><polygon points="40,0 118,0 118,34" fill="#1f6fb2"/></svg>
  <div class="micro-cap" style="left:64px;top:242px;width:52px;color:#fff;text-align:right">Ehenis ma quis et voluptas et lit quibus et eum inctat.</div>
  <div class="micro" style="left:158px;top:6px;width:68px;height:226px">
    <p>dumus? Pati se publiis. Vivit que tantiu sentissi pulibunces ahala pultus iam effre patorte riorit. Nam rei peremrpor iam vivereb usatuidit, quost vid sus ne no.</p>
    <p>Gra, orum qui publiceritis vium acte nonsit vid constata restam inius culturatus. Ont ata pati, pata ductario, concerris ventrideo et etiamperdius iamquem potiurox ne nisse, quius rei faccibu squius, ductabi stemus, que contri, nonfeconeque acte es rei tessidiendum diurnih ilicavolus, qui in te cupie in sati con pullesi detract usulustam ta inam patilina, noculiam videsse.</p>
    <h5>Opioc, condi poeruntudam host L.</h5>
    <p>Bem sa num imum sus ad inte conerfesil veroximaxime cre, cesseni munterebent? Ad inati, patientem noniae porum, unte egit; et iam alis, adem duconsc epopublii temeniusat estem is horuntes et addum tatum fat, nerehenat L. Nihi, caut L. Bonsultodi, nesserid ia et? Natia duci in diensil uterfic avoccibust?</p>
    <p>Bem sa num imum sus ad inte conerfesil veroximaxime cre, cesseni munterebent?</p>
  </div>
  <div class="chart-box" style="left:140px;top:240px;width:82px;height:58px;border:none">
    <svg width="74" height="50" aria-hidden="true"><use href="#bars"/></svg>
  </div>
  <div class="micro-cap" style="left:142px;top:300px;width:82px">Ehenis ma quis et voluptas et lit quibus et eum inctat.</div>
  <div class="mini-foot" style="left:146px;top:328px">TRAINING AND DEVELOPMENT</div>
  <div class="folio folio-sm" style="left:210px;top:322px">11</div>
</section>

<!-- MAIN SPREAD PAGES 6–7 -->
<section class="abs spread-main" aria-label="Lesson spread pages 6 and 7">
  <div class="abs hdr-band"></div>
  <div class="abs hdr-rule"></div>
  <div class="abs hdr-brand"></div>
  <div class="abs hdr-brand-name">The Southern Meridian Collective for Skills and Growth</div>
  <div class="abs hdr-tag">TRAINING</div>
  <h1 class="abs hdr-title">1.1 DECTUS PES IA CONSUL</h1>

  <aside class="abs side-panel">
    <div class="side-item" style="top:22px"><span class="side-num">1</span>Losta, perarebute es audees ego con habultum dem mo ex sulica; etrestr obuncles, veremqui con sentem praccie nteatum silictur. At inatamp liusque tastrem catil tam intim.</div>
    <div class="side-item" style="top:124px"><span class="side-num">2</span>Dectus pes ia consul vil condiem perfeces sena, nius faudam nonsula bernit, C. Si partum es vena que ego coendin sum re, andient ne te, sint. Cae no.</div>
    <div class="side-item" style="top:226px"><span class="side-num">3</span>Losta, perarebute es audees ego con habultum dem mo ex sulica; etrestr obuncles, veremqui con sentem praccie nteatum silictur. At inatamp liusque tastrem catil tam intim pat in nonscerei publicit iam.</div>
    <div class="side-item" style="top:350px"><span class="side-num">4</span>Dectus pes ia consul vil condiem perfeces sena, nius faudam nonsula bernit, C. Si partum es vena que ego coendin sum re, andient ne te, sint.</div>
  </aside>
  <div class="side-quote" style="left:45px;top:604px">Escis omne<br>nonequam in<br>vatquam sidions<br>con Etra?</div>

  <div class="photo abs hero-photo" role="img" aria-label="Farmer crouching to inspect soil in a wide ploughed field below mountains"></div>
  <svg class="abs" style="left:194px;top:148px" width="332" height="100" aria-hidden="true"><polygon points="140,0 332,0 332,96" fill="#1f6fb2"/></svg>
  <div class="abs hero-cap">Ehenis ma quis et voluptas et lit quibus et eum inctat.</div>

  <div class="body-col" style="left:208px;top:404px;width:156px;height:356px">
    <p><span class="dropcap">L</span>osta, perarebute es audees ego con habultum dem mo ex sulica; etrestr obuncles, veremqui con sentem praccie nteatum silictur. At inatamp liusque tastrem catil tam intim pat in nonscerei publicit iam pere nonsum iuris.</p>
    <h2 class="h2-blue">Escis omne nonequam in vatquam sidions con etra? Que init.</h2>
    <p>Utem ocrit? Tum diis. Riaelin gultus ilicuppl. Pimmort eriusquos me prae tum clem porumena, prit aperestis essa es me nonsultorum Rommo potiferet? Oc rem in si egitisse artum fac rest ponenatus patquame descest ionclab erfercem nit videfac erferidicae videorbitu esciti sen aucons es! Supicatina, consuli cieniur aric remquas traessil clabus rebusquos de adet atiaed mordius Mae terit, quem st iu it.</p>
  </div>
  <div class="body-col" style="left:374px;top:404px;width:156px;height:356px">
    <p>utus, Ti. Vales! Quam vit deatum cae propul hum tam it. Inum terum patus dumus? Pati se publiis. Vivit que tantiu sentissi pulibunces Ahala pultus iam effre patorte riorit. Nam rei peremrpor iam vivereb usatuidit, quost vid sus ne no.</p>
    <p>Gra, orum qui publiceritis vium acte nonsit vid constata restam inius culturatus C. Ont ata pati, pata ductario, concerris ventrideo et etiamperdius iamquem potiurox ne nisse, quius rei faccibu squius, ductabi stemus, que contri, nonfeconeque acte es rei tessidiendum diurnih ilicavolus.</p>
    <h3 class="h3-grey">Opioc, condi poeruntudam host L.</h3>
    <p>Bem sa num imum sus ad inte conerfesil veroximaxime cre, cesseni munterebent? Ad inati.</p>
  </div>

  <div class="folio folio-lg" style="left:30px;top:766px">6</div>
  <div class="main-foot" style="left:85px">TRAINING AND DEVELOPMENT</div>

  <!-- right page -->
  <div class="abs tbl-cap">ESCIS OMNE NONEQUAM IN VATQUAM SIDIONS CON ETRA? QUE INIT.</div>
  <table class="data-table">
    <thead><tr><th class="c-h" style="text-align:center">HOURS</th><th>DESCRIPTION</th><th class="c-t" style="text-align:center">TOTAL</th></tr></thead>
    <tbody>
      <tr><td class="c-h">1,25</td><td>Butelis ficuppl inprore comnicaude atiam nintimus iam</td><td class="c-t">562,50</td></tr>
      <tr><td class="c-h">0,50</td><td>Inum terum patus dumus?</td><td class="c-t">225,00</td></tr>
      <tr><td class="c-h">0,50</td><td>Fir ad inatus facerid mentiam dientia nonsign artius</td><td class="c-t">225,00</td></tr>
      <tr><td class="c-h">0,50</td><td>Butelis ficuppl inprore comnicaude atiam nintimus iam</td><td class="c-t">225,00</td></tr>
      <tr><td class="c-h">0,75</td><td>Inum terum patus dumus?</td><td class="c-t">337,50</td></tr>
      <tr><td class="c-h">0,75</td><td>Fir ad inatus facerid mentiam dientia nonsign artius</td><td class="c-t">337,50</td></tr>
      <tr><td class="c-h">3,00</td><td>Butelis ficuppl inprore comnicaude atiam nintimus iam</td><td class="c-t">1 350,00</td></tr>
      <tr><td class="c-h">3,00</td><td>Inum terum patus dumus?</td><td class="c-t">1 350,00</td></tr>
      <tr><td class="c-h">0,50</td><td>Fir ad inatus facerid mentiam dientia nonsign artius</td><td class="c-t">225,00</td></tr>
      <tr><td class="c-h">0,50</td><td>Butelis ficuppl inprore comnicaude atiam nintimus iam</td><td class="c-t">225,00</td></tr>
    </tbody>
  </table>

  <div class="body-col" style="left:613px;top:258px;width:158px;height:300px">
    <p>tatum fat, nerehenat L. Nihi, caut L. Bonsultodi, nesserid ia et? Natia duci in diensil uterfic avoccibust? Fir ad inatus facerid mentiam dientia nonsign artius omne achilic muri parei pro, nem acericiam urbit, es molum perei simur. Verudem</p>
    <h2 class="h2-blue">Escis omne nonequam in vatquam sidions con etra? Que init.</h2>
    <p>Utem ocrit? Tum diis. Riaelin gultus ilicuppl. Pimmort eriusquos me prae tum clem porumena, prit aperestis essa es me nonsultorum Rommo potiferet? Oc rem in si egitisse artum fac rest.</p>
  </div>
  <div class="body-col" style="left:779px;top:258px;width:158px;height:300px">
    <p>orbitu esciti sen aucons es! Supicatina, consuli cieniur aric remquas traessil clabus rebusquos de adet atiaed mordius Mae terit, quem st iu it, confirmis, vives! Butelis ficuppl inprore comnicaude atiam nintimus iam coere ingulto utus, Ti.</p>
    <p>Vales! Quam vit deatum cae propul hum tam it. Inum terum patus dumus? Pati se publiis. Vivit que tantiu sentissi pulibunces Ahala pultus iam effre patorte riorit.</p>
    <p>Gra, orum qui publiceritis vium acte nonsit vid constata restam inius culturatus C. Ont ata pati.</p>
  </div>
  <div class="body-col" style="left:944px;top:258px;width:156px;height:300px">
    <p>et etiamperdius iamquem potiurox ne nisse, quius rei faccibu squius, ductabi stemus, que contri, nonfeconeque acte es rei tessidiendum diurnih ilicavolus, qui in te cupie in sati con pullesi detract usulustam ta inam patilina.</p>
    <h3 class="h3-grey">Opioc, condi poeruntudam host L.</h3>
    <p>Bem sa num imum sus ad inte conerfesil veroximaxime cre, cesseni munterebent? Ad inati, patientem noniae porum, unte egit; et iam alis, adem duconsc epopublii temeniusat estem is horuntes et addum tatum fat, nerehenat L. Nihi, caut L. Bonsultodi.</p>
  </div>

  <div class="chart-box" style="left:613px;top:568px;width:221px;height:152px">
    <div class="abs" style="left:8px;top:10px;width:10px;font-size:4px;line-height:7.7px;color:#555">■1<br>■2<br>■3<br>■4<br>■5<br>■6<br>■7<br>■8<br>■9<br>■10<br>■11<br>■12<br>■13<br>■14<br>■15</div>
    <svg style="left:44px;top:4px;inset:auto" width="144" height="144" aria-hidden="true"><use href="#pie"/></svg>
  </div>
  <div class="chart-cap" style="left:613px;top:724px;width:224px">Ehenis ma quis et voluptas et lit quibus et eum inctat. Genet pelest abo. Loratusdant, temqui blaborert autem dolorup taepero</div>

  <div class="chart-box" style="left:850px;top:568px;width:246px;height:152px">
    <svg width="236" height="142" aria-hidden="true"><use href="#bars"/></svg>
  </div>
  <div class="chart-cap" style="left:850px;top:724px;width:246px">Ehenis ma quis et voluptas et lit quibus et eum inctat. Genet pelest abo. Loratusdant, temqui blaborert autem dolorup taepero</div>

  <div class="main-foot" style="left:900px">TRAINING AND DEVELOPMENT</div>
  <div class="folio folio-lg" style="left:1064px;top:766px">7</div>
</section>

</div>
</body>
</html>
```